Rugged Postcard Design for Contractors

Dorrit Whelan Insurance is a commercial lines agency that is based out of Florida that specializes in contractors insurance. Are markets include service and installation for HVAC, Plumbing, Concrete, Electrical and Roofing. We market throughout the State of Florida with monthly postcards We are looking for a designer that can encompass all of our Target Markets in one postcard design.

Target Market(s)

Contractors: HVAC, Plumbers, Concrete, Electrical, Roofing

Industry/Entity Type

Concrete

Requirements
Must have
• Huge Contractor Savings
• We will help you choose your customized policy features: Bonds (Bid/Performance/Payment), Fleet Coverage is Available, Blanket Additional Insured , Workers Compensation, Package Discounts, Installation Floaters, Specialty Contractor Enhancement Endorsements
• Consistent Pricing and Long Term Savings
• General Liability at Preferred Rates
• Don't Miss This Opportunity to Save 35% or More
• (850) 472-6158
• www.DorritWhelan.example
• Size: 6 x 9
• With bleed
• full color both sides
Nice to have
• Rugged designs
• Blacks, Yellows, and Oranges for color

```html
<!DOCTYPE html>
<html lang="en">
<head>
<meta charset="utf-8">
<title>Dorrit Whelan Insurance – Contractor Postcard</title>
<link href="https://fonts.googleapis.com/css2?family=Arimo:wght@400;700&family=Open+Sans:wght@400;700;800&display=swap" rel="stylesheet">
<style>
  :root{
    --yellow:#f8b133;
    --ink:#2f2f31;
    --charcoal:#3d3d3f;
    --slate:#8d8d90;
    --black:#141414;
    --paper:#ffffff;
    --mist:#f1f1f2;
    --rule:#c9c9cb;
    --stage:#e9e6e1;
    --muted:#777777;
  }
  *{box-sizing:border-box;margin:0;padding:0}
  html,body{width:1200px;height:699px;overflow:hidden;background:var(--stage)}
  body{position:relative;font-family:"Arimo",Arial,sans-serif;color:var(--ink)}
  .card{position:absolute;background:var(--paper);box-shadow:0 2px 6px rgba(0,0,0,.25);overflow:hidden}
  .abs{position:absolute}

  /* brand */
  .brand{position:absolute;display:flex;align-items:center;gap:10px}
  .brand-mark{width:14px;height:14px;background:var(--charcoal)}
  .brand-name{font-weight:400;color:var(--charcoal);letter-spacing:2px;text-transform:uppercase;white-space:nowrap}

  /* front */
  .front{left:20px;top:20px;width:423px;height:644px;background:var(--mist)}
  .front .head{left:0;top:0;width:423px;height:75px;background:var(--paper)}
  .front .head-rule{left:0;top:75px;width:423px;height:4px;background:var(--charcoal)}
  .front .photo{left:0;top:79px;width:423px;height:256px;background:linear-gradient(160deg,#bcd0dd 0%,#9fb4c4 40%,#3a4a63 75%,#27324a 100%)}
  .trades{left:14px;top:90px;list-style:none;font-family:"Open Sans",sans-serif;font-weight:800;font-size:18px;line-height:20.5px;color:var(--black)}
  .savings-band{left:0;top:334px;width:272px;height:38px}
  .savings-title{left:17px;top:339px;font-family:"Open Sans",sans-serif;font-size:16px;color:var(--yellow);white-space:nowrap}
  .intro{left:22px;top:389px;font-size:12px;color:var(--ink);white-space:nowrap}
  .features{left:22px;top:414px;list-style:none;font-size:12px;color:var(--ink)}
  .features li{display:flex;align-items:center;gap:6px;height:23.6px;white-space:nowrap}
  .features .muted{color:var(--muted)}
  .dot{width:12px;height:12px;border-radius:50%;background:var(--yellow);display:inline-flex;align-items:center;justify-content:center;flex:none}
  .panels{left:0;top:0}
  .pricing{left:313px;top:384px;width:114px;text-align:center;font-size:11px;line-height:15px;color:#fff;white-space:nowrap}
  .offer{left:282px;top:486px;width:140px;text-align:center;font-size:11.5px;line-height:15px;color:var(--yellow);white-space:nowrap}
  .offer .gap{display:block;height:21px}
  .offer .big{font-size:15px;line-height:18px}
  .footer-bar{left:0;top:608px;width:423px;height:36px}
  .phone{left:22px;top:612px;font-size:12.5px;color:var(--black);display:flex;align-items:center;gap:5px;white-space:nowrap}
  .web{left:232px;top:619px;font-size:12px;color:#fff;white-space:nowrap}

  /* back */
  .back{left:532px;top:244px;width:633px;height:420px;background:#f4f4f4}
  .back .panel{left:0;top:0;width:320px;height:353px;background:var(--paper)}
  .back .head-rule{left:0;top:71px;width:320px;height:5px;background:var(--charcoal)}
  .back .photo{left:0;top:76px;width:320px;height:83px;background:linear-gradient(100deg,#f2b43a 0%,#d9a066 22%,#efe6dc 55%,#f7f5f2 100%)}
  .about{left:18px;top:169px;width:298px;font-size:7.3px;line-height:9.5px;color:var(--ink)}
  .about b{font-weight:700}
  .markets{left:18px;top:202px;font-size:7.3px;color:var(--ink);white-space:nowrap}
  .markets-list{left:18px;top:213px;font-size:9.6px;color:var(--black);white-space:nowrap}
  .grey-block{left:0;top:233px;width:320px;height:86px;background:var(--slate)}
  .grey-copy{left:0;top:243px;width:320px;text-align:center;font-size:9.6px;line-height:17px;color:var(--yellow)}
  .grey-cta{left:0;top:283px;width:320px;text-align:center;font-size:11.5px;line-height:13px;color:var(--charcoal)}
  .grey-cta .big{font-size:14px;line-height:15px}
  .back-footer{left:0;top:319px;width:320px;height:34px}
  .back-phone{left:22px;top:322px;font-size:11.5px;color:var(--black);display:flex;align-items:center;gap:4px;white-space:nowrap}
  .back-web{left:158px;top:329px;font-size:11.5px;color:#fff;white-space:nowrap}
  .stamp{left:523px;top:22px;width:86px;height:61px;border:1px solid #bdbdbd;background:#f7f7f7}
  .address-line{left:375px;width:233px;height:1px;background:var(--rule)}
</style>
</head>
<body>

  <section class="card front" aria-label="Postcard front">
    <div class="abs head"></div>
    <div class="brand" style="left:24px;top:29px">
      <span class="brand-mark"></span>
      <span class="brand-name" style="font-size:15px">Dorrit Whelan Insurance</span>
    </div>
    <div class="abs head-rule"></div>
    <div class="abs photo" role="img" aria-label="Smiling contractor in a yellow hard hat carrying lumber, with a crew of workers in a city behind him"></div>

    <ul class="abs trades">
      <li>» HVAC</li>
      <li>» Plumbers</li>
      <li>» Concrete</li>
      <li>» Electrical</li>
      <li>» Roofing</li>
    </ul>

    <svg class="abs savings-band" viewBox="0 0 272 38" aria-hidden="true">
      <polygon points="0,0 252,0 272,38 0,38" fill="#3d3d3f"/>
    </svg>
    <div class="abs savings-title">Huge Contractor Savings</div>

    <svg class="abs panels" width="423" height="644" viewBox="0 0 423 644" aria-hidden="true">
      <polygon points="332,356 423,356 423,460 302,460" fill="#8d8d90"/>
      <polygon points="302,468 423,468 423,608 263,608" fill="#3d3d3f"/>
    </svg>
    <div class="abs pricing">Consistent Pricing<br>and<br>Long Term Savings</div>
    <div class="abs offer">
      General Liability<br>at Preferred Rates
      <span class="gap"></span>
      Don't Miss This<br>Opportunity to<br>
      <span class="big">Save 35% or More</span>
    </div>

    <p class="abs intro">We will help you choose your customized policy features:</p>
    <ul class="abs features">
      <li><span class="dot"><svg width="6" height="6" viewBox="0 0 6 6"><path d="M2 1l2 2-2 2" stroke="#fff" stroke-width="1.2" fill="none"/></svg></span><span>Bonds <span class="muted">(Bid/Performance/Payment)</span></span></li>
      <li><span class="dot"><svg width="6" height="6" viewBox="0 0 6 6"><path d="M2 1l2 2-2 2" stroke="#fff" stroke-width="1.2" fill="none"/></svg></span><span>Fleet Coverage is Available</span></li>
      <li><span class="dot"><svg width="6" height="6" viewBox="0 0 6 6"><path d="M2 1l2 2-2 2" stroke="#fff" stroke-width="1.2" fill="none"/></svg></span><span>Blanket Additional Insured</span></li>
      <li><span class="dot"><svg width="6" height="6" viewBox="0 0 6 6"><path d="M2 1l2 2-2 2" stroke="#fff" stroke-width="1.2" fill="none"/></svg></span><span>Workers Compensation</span></li>
      <li><span class="dot"><svg width="6" height="6" viewBox="0 0 6 6"><path d="M2 1l2 2-2 2" stroke="#fff" stroke-width="1.2" fill="none"/></svg></span><span>Package Discounts</span></li>
      <li><span class="dot"><svg width="6" height="6" viewBox="0 0 6 6"><path d="M2 1l2 2-2 2" stroke="#fff" stroke-width="1.2" fill="none"/></svg></span><span>Installation Floaters</span></li>
      <li><span class="dot"><svg width="6" height="6" viewBox="0 0 6 6"><path d="M2 1l2 2-2 2" stroke="#fff" stroke-width="1.2" fill="none"/></svg></span><span>Specialty Contractor</span></li>
      <li><span class="dot"><svg width="6" height="6" viewBox="0 0 6 6"><path d="M2 1l2 2-2 2" stroke="#fff" stroke-width="1.2" fill="none"/></svg></span><span>Enhancement Endorsements</span></li>
    </ul>

    <svg class="abs footer-bar" viewBox="0 0 423 36" aria-hidden="true">
      <rect x="0" y="0" width="423" height="36" fill="#141414"/>
      <polygon points="0,0 195,0 180,22 0,22" fill="#f8b133"/>
    </svg>
    <div class="abs phone">
      <svg width="12" height="12" viewBox="0 0 12 12" aria-hidden="true"><circle cx="6" cy="6" r="5.3" fill="none" stroke="#141414" stroke-width="1.2"/><path d="M4 3.2c-.6.6-.4 2 .8 3.3s2.6 1.6 3.2 1l.5-.6-1.2-1-.6.5C6 6 5.6 5.6 5.2 5l.5-.6-1-1.2z" fill="#141414"/></svg>
      (850) 472-6158
    </div>
    <div class="abs web">www.DorritWhelan.example</div>
  </section>

  <section class="card back" aria-label="Postcard back">
    <div class="abs panel"></div>
    <div class="brand" style="left:18px;top:26px">
      <span class="brand-mark"></span>
      <span class="brand-name" style="font-size:13.5px">Dorrit Whelan Insurance</span>
    </div>
    <div class="abs head-rule"></div>
    <div class="abs photo" role="img" aria-label="Contractor's hands measuring on a plank beside a yellow hard hat"></div>

    <p class="abs about"><b>Dorrit Whelan Insurance</b> is a commercial lines agency that is based out of Florida that specializes in contractors insurance.</p>
    <p class="abs markets">Are markets include service and installation for:</p>
    <p class="abs markets-list">HVAC, Plumbing, Concrete, Electrical and Roofing</p>

    <div class="abs grey-block"></div>
    <div class="abs grey-copy">Consistent Pricing and Long Term Savings<br>General Liability at Preferred Rates</div>
    <div class="abs grey-cta">Don't Miss This Opportunity to<br><span class="big">Save 35% or More</span></div>

    <svg class="abs back-footer" viewBox="0 0 320 34" aria-hidden="true">
      <rect x="0" y="0" width="320" height="34" fill="#141414"/>
      <polygon points="0,0 152,0 140,17 0,17" fill="#f8b133"/>
    </svg>
    <div class="abs back-phone">
      <svg width="11" height="11" viewBox="0 0 12 12" aria-hidden="true"><circle cx="6" cy="6" r="5.3" fill="none" stroke="#141414" stroke-width="1.2"/><path d="M4 3.2c-.6.6-.4 2 .8 3.3s2.6 1.6 3.2 1l.5-.6-1.2-1-.6.5C6 6 5.6 5.6 5.2 5l.5-.6-1-1.2z" fill="#141414"/></svg>
      (850) 472-6158
    </div>
    <div class="abs back-web">www.DorritWhelan.example</div>

    <div class="abs stamp" aria-label="Stamp area"></div>
    <div class="abs address-line" style="top:142px"></div>
    <div class="abs address-line" style="top:172px"></div>
    <div class="abs address-line" style="top:202px"></div>
    <div class="abs address-line" style="top:232px"></div>
    <div class="abs address-line" style="top:261px"></div>
  </section>

</body>
</html>
```